Company Proposal Powerpoint Template

We would like to update our overall proposal presentation with a fresh, new look that might appeal to the younger generation. We are a full-meeting management company that specializes in corporate events sales meetings, incentive trips, and tradeshows/conferences.
We have a core set of slides that we use for presentations, but will also need to customize based on the customers we service and what we are selling each potential client.
We have a company logo, but we are not tied into the colors schemes for the logo and are okay adding the logo in black or white versus in color.
I have included our current look and feel for this presentation. This will also give you content that we typically add to this presentation.
Reason: Traveling out of the office so limited access to review the art.
Industry/Entity Type
It Company
Look and feel
Each slider illustrates characteristics of the customer's brand and the style your logo design should communicate.

```html
<!DOCTYPE html>
<html lang="en">
<head>
<meta charset="utf-8">
<title>Nexa Events – Proposal Slides</title>
<link href="https://fonts.googleapis.com/css2?family=Bebas+Neue&family=Open+Sans:wght@300;400;600&display=swap" rel="stylesheet">
<style>
  :root {
    --page: #f3f3f4;
    --cyan: #1aa3dc;
    --mid: #5b6cc1;
    --purple: #7232a3;
    --swot-core: #6449b2;
    --white: #ffffff;
    --pill-text: #5a3f98;
    --ring: #d9d9de;
    --label: #4a4a55;
    --social-1: #1e8fe0;
    --social-2: #7cc242;
    --social-3: #f2c21b;
    --portrait-a: #8a7a70;
    --portrait-b: #3a302c;
  }
  * { box-sizing: border-box; margin: 0; padding: 0; }
  html, body { width: 714px; height: 1200px; overflow: hidden; background: var(--page); }
  body { position: relative; font-family: "Open Sans", sans-serif; color: var(--white); }

  .slide {
    position: absolute; left: 19px; width: 674px; height: 379px;
    background: linear-gradient(90deg, var(--cyan) 0%, var(--mid) 52%, var(--purple) 100%);
    overflow: hidden;
  }
  .slide--swot { top: 14px; }
  .slide--team { top: 414px; }
  .slide--services { top: 814px; }

  .slide-title {
    position: absolute; left: 34px; top: 44px;
    font-family: "Bebas Neue", sans-serif; font-weight: 400;
    font-size: 47px; line-height: 1; letter-spacing: 0.5px;
  }

  .brand {
    position: absolute; right: 26px; bottom: 14px;
    display: flex; align-items: center; gap: 5px;
    font-family: "Open Sans", sans-serif; font-weight: 400; font-size: 10px; color: var(--white);
  }
  .brand-mark { width: 12px; height: 12px; border: 1.5px solid var(--white); }

  /* SWOT slide */
  .swot-item { position: absolute; width: 140px; }
  .swot-item--s { left: 40px; top: 116px; }
  .swot-item--w { left: 191px; top: 116px; }
  .swot-item--t { left: 40px; top: 226px; }
  .swot-item--o { left: 191px; top: 226px; }
  .pill {
    display: inline-block; background: var(--white); color: var(--pill-text);
    border-radius: 12px; padding: 4px 12px; font-size: 9px; letter-spacing: 0.3px;
  }
  .swot-heading { margin-top: 7px; font-weight: 300; font-size: 12px; }
  .swot-body { margin-top: 6px; font-weight: 300; font-size: 8.6px; line-height: 12px; }
  .swot-graphic { position: absolute; left: 405px; top: 102px; }

  /* Team slide */
  .team { position: absolute; top: 134px; left: 0; width: 674px; }
  .member { position: absolute; width: 130px; margin-left: -65px; text-align: center; }
  .portrait {
    width: 108px; height: 108px; border-radius: 50%; margin: 0 auto;
    background: radial-gradient(circle at 50% 40%, var(--portrait-a), var(--portrait-b));
  }
  .member-name { margin-top: 7px; font-size: 14px; font-weight: 400; }
  .member-role { margin-top: 1px; font-size: 9px; font-weight: 300; }
  .socials { display: flex; justify-content: center; gap: 8px; margin-top: 6px; }
  .social { width: 26px; height: 26px; border-radius: 50%; }
  .social--a { background: var(--social-1); }
  .social--b { background: var(--social-2); }
  .social--c { background: var(--social-3); }

  /* Services slide */
  .services-heading { position: absolute; left: 41px; top: 110px; font-size: 14px; font-weight: 300; letter-spacing: 0.2px; }
  .service-list { position: absolute; left: 60px; top: 137px; list-style: none; }
  .service-list li { height: 25.3px; font-size: 12.4px; font-weight: 300; padding-left: 15px; position: relative; }
  .service-list li::before { content: "›"; position: absolute; left: 0; top: -1px; font-size: 13px; }
  .cycle { position: absolute; left: 439px; top: 108px; }
  .cycle-label { font-family: "Open Sans", sans-serif; font-size: 7.4px; font-weight: 600; }
</style>
</head>
<body>

<section class="slide slide--swot">
  <h1 class="slide-title">Global Experience</h1>

  <div class="swot-item swot-item--s">
    <span class="pill">STRENGTH</span>
    <p class="swot-heading">Title text demo</p>
    <p class="swot-body">Lorem ipsum dolor sit amet, consectetur adipiscing elit, incididunt ut labore et dolore</p>
  </div>
  <div class="swot-item swot-item--w">
    <span class="pill">WEAKNESS</span>
    <p class="swot-heading">Title text demo</p>
    <p class="swot-body">Lorem ipsum dolor sit amet, consectetur adipiscing elit, incididunt ut labore et dolore</p>
  </div>
  <div class="swot-item swot-item--t">
    <span class="pill">THREAT</span>
    <p class="swot-heading">Title text demo</p>
    <p class="swot-body">Lorem ipsum dolor sit amet, consectetur adipiscing elit, incididunt ut labore et dolore</p>
  </div>
  <div class="swot-item swot-item--o">
    <span class="pill">OPPORTUNITIES</span>
    <p class="swot-heading">Title text demo</p>
    <p class="swot-body">Lorem ipsum dolor sit amet, consectetur adipiscing elit, incididunt ut labore et dolore</p>
  </div>

  <svg class="swot-graphic" width="220" height="220" viewBox="0 0 220 220">
    <g fill="#ffffff">
      <rect x="0" y="0" width="86" height="86" rx="7"/>
      <rect x="134" y="0" width="86" height="86" rx="7"/>
      <rect x="0" y="134" width="86" height="86" rx="7"/>
      <rect x="134" y="134" width="86" height="86" rx="7"/>
      <polygon points="80,20 120,20 140,43 120,66 80,66 100,43"/>
      <polygon points="100,154 140,154 120,177 140,200 100,200 80,177"/>
      <polygon points="20,140 20,100 43,80 66,100 66,140"/>
      <polygon points="154,80 154,120 177,140 200,120 200,80"/>
    </g>
    <rect x="58" y="88" width="104" height="44" fill="var(--swot-core)"/>
    <g fill="var(--swot-core)" font-family="Open Sans, sans-serif" font-weight="300" text-anchor="middle">
      <text x="40" y="62" font-size="40">S</text>
      <text x="180" y="62" font-size="40">W</text>
      <text x="40" y="196" font-size="40">T</text>
      <text x="180" y="196" font-size="40">O</text>
    </g>
    <text x="110" y="119" fill="#ffffff" font-family="Open Sans, sans-serif" font-weight="300" font-size="27" text-anchor="middle">SWOT</text>
  </svg>

  <div class="brand"><span class="brand-mark"></span>Nexa Events</div>
</section>

<section class="slide slide--team">
  <h1 class="slide-title">Your Nexa Team</h1>
  <div class="team">
    <div class="member" style="left:74px">
      <div class="portrait" role="img" aria-label="Portrait photo of Mara Ellison"></div>
      <p class="member-name">Mara Ellison</p>
      <p class="member-role">Vice President</p>
      <div class="socials"><span class="social social--a"></span><span class="social social--b"></span><span class="social social--c"></span></div>
    </div>
    <div class="member" style="left:206px">
      <div class="portrait" role="img" aria-label="Portrait photo of Jenna Holt"></div>
      <p class="member-name">Jenna Holt</p>
      <p class="member-role">Sales</p>
      <div class="socials"><span class="social social--a"></span><span class="social social--b"></span><span class="social social--c"></span></div>
    </div>
    <div class="member" style="left:337px">
      <div class="portrait" role="img" aria-label="Portrait photo of Claire Winton"></div>
      <p class="member-name">Claire Winton</p>
      <p class="member-role">Director of Operations</p>
      <div class="socials"><span class="social social--a"></span><span class="social social--b"></span><span class="social social--c"></span></div>
    </div>
    <div class="member" style="left:469px">
      <div class="portrait" role="img" aria-label="Portrait photo of Diane Rowley"></div>
      <p class="member-name">Diane Rowley</p>
      <p class="member-role">Program Director</p>
      <div class="socials"><span class="social social--a"></span><span class="social social--b"></span><span class="social social--c"></span></div>
    </div>
    <div class="member" style="left:600px">
      <div class="portrait" role="img" aria-label="Portrait photo of Owen Brennick"></div>
      <p class="member-name">Owen Brennick</p>
      <p class="member-role">Director of Technology</p>
      <div class="socials"><span class="social social--a"></span><span class="social social--b"></span><span class="social social--c"></span></div>
    </div>
  </div>
  <div class="brand"><span class="brand-mark"></span>Nexa Events</div>
</section>

<section class="slide slide--services">
  <h1 class="slide-title">Global Experience</h1>
  <h2 class="services-heading">EVENT MANAGEMENT SERVICES</h2>
  <ul class="service-list">
    <li>Overall Logistics &amp; Event Coordination, BEOs, Timelines</li>
    <li>Supplier Management, Contracting, Payment Schedules</li>
    <li>Conference/Program Promotion, Marketing Plans</li>
    <li>Production, Entertainment, Speakers</li>
    <li>Tradeshow Management, Sponsor &amp; Exhibit Sales</li>
    <li>Air Ticketing &amp; Ground Transportation</li>
    <li>Off-Site Events, including Tours &amp; Recreational Activities</li>
    <li>Financial Management &amp; Post-Program Reconciliation</li>
    <li>Gifts, Amenities, Awards, Hospitality Desks, Team Buildings, and more...</li>
  </ul>

  <svg class="cycle" width="220" height="220" viewBox="0 0 220 220">
    <g fill="none" stroke="var(--ring)" stroke-width="8">
      <path d="M125.3,23.3 A88 88 0 0 1 189.8,147.2"/>
      <path d="M177.4,166.6 A88 88 0 0 1 37.9,160.5"/>
      <path d="M27.3,140.1 A88 88 0 0 1 102.3,22.3"/>
    </g>
    <g fill="var(--ring)">
      <polygon points="-7,-9 7,0 -7,9" transform="translate(189.8,147.2) rotate(115)"/>
      <polygon points="-7,-9 7,0 -7,9" transform="translate(37.9,160.5) rotate(235)"/>
      <polygon points="-7,-9 7,0 -7,9" transform="translate(102.3,22.3) rotate(355)"/>
    </g>
    <circle cx="110" cy="110" r="74" fill="#ffffff"/>
    <path d="M110,110 L110,36 A74 74 0 0 1 174.1,147 Z" fill="var(--cyan)"/>
    <g stroke="var(--swot-core)" stroke-width="5">
      <line x1="110" y1="110" x2="110" y2="34"/>
      <line x1="110" y1="110" x2="176" y2="148"/>
      <line x1="110" y1="110" x2="44" y2="148"/>
    </g>
    <g class="cycle-label" text-anchor="middle">
      <text x="70" y="90" fill="var(--label)">ONSITE EVENT</text>
      <text x="70" y="100" fill="var(--label)">MANAGEMENT</text>
      <text x="149" y="86" fill="#ffffff">EVENT</text>
      <text x="149" y="96" fill="#ffffff">MANAGEMENT</text>
      <text x="149" y="106" fill="#ffffff">SERVICES</text>
      <text x="110" y="168" fill="var(--label)">REGISTRATION SERVICES</text>
    </g>
  </svg>

  <div class="brand"><span class="brand-mark"></span>Nexa Events</div>
</section>

</body>
</html>
```